PIPE RELINING COMPANY NEEDS A NEW INFORMATIVE FLYER CREATED

We are a company that sells a service to residential homeowners (using a particular state of the art international product) and we need to refresh our A4 tri- fold flyer (z fold 6 pages). The layout needs to include pictures, heading and text boxes, but be simple and clean cut at the same time.

The front of the flyer must have the attached picture of the pipe under the house, logo and website.

This flyer is going to be given to clients and to leave with them when we quote for work.

Our colour scheme is black, white, red. A highlight colour if needed (in small amounts) could be 100% cyan and also a bright orange.

I have attached the copy of the text and this can be spread out throughout the brochure.

We are a professional and industry leading company so it needs to be professional, clean cut but with a modern edge.

Target Market(s)

HOMEOWNERS

Industry/Entity Type

It Company

Font styles to use
Sans Serif

Colors
ec1f27
ffffff
000000
f37122

Requirements
Must have
• PROFESSINAL, MODERN
• USE OF BLACK, RED AND WHITE - REFER LOGO
Should not have
• BE CLUTTERED

```html
<!DOCTYPE html>
<html lang="en">
<head>
<meta charset="utf-8">
<title>Linewell Trifold Brochure – Inside</title>
<link href="https://fonts.googleapis.com/css2?family=Lato:ital,wght@0,400;0,700;1,300;1,400&display=swap" rel="stylesheet">
<style>
  :root{
    --red:#ec1f27;
    --orange:#f37122;
    --cyan:#1e9ad6;
    --black:#000;
    --ink:#222;
    --white:#fff;
    --canvas:#bcbdc0;
    --label:#6d6e71;
  }
  *{box-sizing:border-box;margin:0;padding:0}
  html,body{width:1200px;height:980px;overflow:hidden}
  body{background:var(--canvas);font-family:"Lato",sans-serif;color:var(--ink);position:relative}
  .sheet-label{position:absolute;left:37px;top:32px;font-size:27px;font-weight:700;color:var(--label);letter-spacing:.2px}
  .brochure{position:absolute;left:45px;top:73px;width:1113px;height:865px;background:var(--white)}
  .panel{position:absolute;top:0;height:865px}
  .panel--left{left:0;width:371px}
  .panel--middle{left:371px;width:372px}
  .panel--right{left:743px;width:370px;background:var(--black);color:var(--white)}
  .photo{position:absolute}
  .tab{position:absolute;height:40px;display:flex;align-items:center;font-style:italic;font-weight:400;font-size:20px;color:var(--white);background:#1a1a1a;border-radius:0 6px 6px 0;padding-left:35px}
  .tab--red{background:var(--red)}
  /* left */
  .hero{left:0;top:0;width:371px;height:210px;background:linear-gradient(180deg,#c9d3d8 0%,#b9c1c4 40%,#a68a5e 55%,#c9a673 100%)}
  .why-tab{left:0;top:192px;width:170px;background:#1a1a1a;padding-left:35px;font-size:19px}
  .why{position:absolute;left:34px;top:252px;width:310px;font-size:12px;line-height:15px}
  .why h3{color:var(--orange);font-size:12.5px;font-weight:700;line-height:15px;text-transform:uppercase;margin-bottom:14px}
  .why p{margin-bottom:14px}
  .warranty{display:flex;gap:12px;align-items:center}
  .warranty p{width:200px}
  .footer{position:absolute;left:0;bottom:0;width:100%;height:101px;background:var(--black);padding:10px 0 0 34px}
  .footer__tag{font-style:italic;font-weight:300;font-size:21px;line-height:21px;color:var(--white)}
  .footer__url{margin-top:11px;color:var(--red);font-size:13px;letter-spacing:3.4px;font-style:italic}
  /* middle */
  .mid-tab{left:0;top:32px;width:317px;font-size:19px;background:#1a1a1a}
  .benefits{position:absolute;left:52px;top:100px;width:300px;list-style:none;font-size:12.2px;line-height:18px;color:#333}
  .benefits li{position:relative;padding-left:19px}
  .benefits li::before{content:"";position:absolute;left:0;top:6px;width:5px;height:5px;border-radius:50%;background:var(--red)}
  .strip{position:absolute;top:264px;left:5px;display:flex;gap:4px}
  .strip figure{position:relative;height:101px}
  .strip figcaption{position:absolute;left:0;bottom:0;width:100%;height:18px;background:var(--red);color:var(--white);font-size:9px;line-height:18px;padding-left:6px}
  .things-tab{left:0;top:393px;width:317px;font-size:19px;background:#1a1a1a}
  .facts{position:absolute;left:35px;top:451px;width:315px;font-size:12.2px;line-height:15px;color:#333}
  .facts h4{color:var(--cyan);font-weight:700;font-size:12.5px;line-height:15px}
  .facts p{margin-bottom:14px}
  /* right */
  .process-tab{left:0;top:32px;width:317px;font-size:19px;padding-left:43px}
  .step{position:absolute;left:37px;width:330px;height:75px}
  .step__photo{position:absolute;left:0;top:0;width:106px;height:75px;border:2px solid var(--red)}
  .step__num{position:absolute;left:14px;top:-13px;width:32px;height:32px;border-radius:50%;background:var(--white);border:2px solid var(--red);color:var(--red);font-size:23px;line-height:28px;text-align:center}
  .step__bracket{position:absolute;left:112px;top:-8px}
  .step__text{position:absolute;left:134px;width:160px;font-size:10.6px;line-height:13.7px;color:var(--white)}
  .result-tab{left:-3px;top:552px;width:147px;font-size:20px;padding-left:45px}
  .result{position:absolute;left:42px;top:605px;width:160px;font-size:10.6px;line-height:13.7px}
  .result-photo{position:absolute;left:214px;top:591px;width:132px;height:93px;border:2px solid var(--red);background:linear-gradient(135deg,#5a4030,#8a6a45 50%,#3fa040 65%,#6b4a30)}
  .result-num{left:78px;top:-22px;width:40px;height:40px;font-size:29px;line-height:35px}
  .panel--right .footer{padding-left:52px;top:764px;height:auto;bottom:auto;background:none}
</style>
</head>
<body>
  <div class="sheet-label">TRIFOLD BROCHURE INSIDE</div>

  <main class="brochure">
    <!-- left panel -->
    <section class="panel panel--left">
      <div class="photo hero" role="img" aria-label="Cutaway illustration of a pipe running underground beneath a house"></div>
      <h2 class="tab why-tab">Why it works</h2>
      <div class="why">
        <h3>Linewell uses epoxy rein not polyester or silicate resins.</h3>
        <p>Why? Because epoxy resin does not shrink. Polyester and silicate resins can shrink in the pipe allowing tree roots to return.</p>
        <h3>Linewell inverts the liner instead of using a drag-in method.</h3>
        <p>Why? Because this means that the resin has contact with the host pipe impregnating the cracks and joins the pipework. With the drag in method, the resin does not have contact with the host pipe and cannot impregnate the cracks and joins.</p>
        <h3>Linewell uses a German system called Relinor.</h3>
        <p>Why? Because it has been extensively tested in Europe and came out as the test winner in standard and extreme conditions based on all assessment criteria – effective-ness, density and load carrying capacity. Relinor has a proven track record and bee used to reline hundreds of kms throughout Europe.</p>
        <h3>Linewell provides a 25 year warranty</h3>
        <div class="warranty">
          <p>Why?&nbsp; Because we understand the quality of the equipment and product and how we install it. We were one of the first to reline in NSW and are constantly carrying out research and development.</p>
          <svg width="100" height="90" viewBox="0 0 100 90" role="img" aria-label="Warranty seal badge">
            <circle cx="50" cy="44" r="40" fill="#f0c23a"/>
            <rect x="2" y="52" width="96" height="16" fill="#c8202a"/>
          </svg>
        </div>
      </div>
      <footer class="footer">
        <p class="footer__tag">A fast, clean, permanent<br>solution for fixing blocked drains.</p>
        <p class="footer__url">www.linewell.com.au</p>
      </footer>
    </section>

    <!-- middle panel -->
    <section class="panel panel--middle">
      <h2 class="tab mid-tab">What Does Pipe Relining Mean?</h2>
      <ul class="benefits">
        <li>Permanent jointless liner</li>
        <li>50 years life expectancy</li>
        <li>Up front price</li>
        <li>Environmentally sound</li>
        <li>Eliminates structural disturbances</li>
        <li>Imprevious to future root penetration</li>
        <li>Provides increased flow characteristics</li>
        <li>Suitable for industrial, residential and commercial applications</li>
      </ul>
      <div class="strip">
        <figure style="width:117px"><div role="img" aria-label="Cracked pipe in soil" style="height:100%;background:linear-gradient(180deg,#4a2a1c,#7a5a48 60%,#3a2218)"></div><figcaption>Common Pipe Issues</figcaption></figure>
        <figure style="width:104px"><div role="img" aria-label="Green liner inside an old pipe" style="height:100%;background:linear-gradient(90deg,#2f8a2a,#6fd24a 50%,#2f8a2a)"></div><figcaption>Pipe inside the old Pipe</figcaption></figure>
        <figure style="width:130px"><div role="img" aria-label="Relined pipe underground among roots" style="height:100%;background:linear-gradient(180deg,#1a120c,#8a6a40 55%,#4a3020)"></div><figcaption>Pipe Relining Underground</figcaption></figure>
      </div>
      <h2 class="tab things-tab">Things your should know</h2>
      <div class="facts">
        <h4>Knowledge &amp; Experience</h4>
        <p>We train other plumbers and have been doing it for over 10 years.</p>
        <h4>We’re An Owned &amp; Operated Business</h4>
        <p>We take great pride in our work. Our business is based on relationships not transactions.</p>
        <h4>We Use the best in class pipe relining solution</h4>
        <p>We have sourced the best products and equipment from around the world and our Flo-Line product is from Germany.</p>
        <h4>We have state of the art equipment.</h4>
        <p>Our truck is customer designed and filly equipped with latest technology to carry out pipe relining.</p>
        <h4>We’re Fully licensed &amp; Insured</h4>
        <p>All of our technicians are fully licensed and qualified to complete the job. Our company is fully insured and are happy to provide you with documentation.</p>
        <h4>After Sales Service</h4>
        <p>We don’t forget about you after the job and as part of the warranty we carry out an annual camera inspection of the drainage.</p>
      </div>
    </section>

    <!-- right panel -->
    <section class="panel panel--right">
      <h2 class="tab tab--red process-tab">Patch Repair Process</h2>

      <div class="step" style="top:102px">
        <div class="step__photo" role="img" aria-label="Service truck with water jetter equipment" style="background:linear-gradient(135deg,#222,#666 50%,#333)"></div>
        <div class="step__num">1</div>
        <svg class="step__bracket" width="14" height="92"><path d="M13 0 L2 12 L2 80 L13 92" fill="none" stroke="#ec1f27" stroke-width="2"/></svg>
        <p class="step__text" style="top:2px">Clean the line with a high pressure water jetter, and carry out a camera inspection to determine the exact location and cause of the problems.</p>
      </div>
      <div class="step" style="top:215px">
        <div class="step__photo" role="img" aria-label="Liner being fed through impregnation machine" style="background:linear-gradient(135deg,#ddd,#999 50%,#3a9a3a)"></div>
        <div class="step__num">2</div>
        <svg class="step__bracket" width="14" height="92"><path d="M13 0 L2 12 L2 80 L13 92" fill="none" stroke="#ec1f27" stroke-width="2"/></svg>
        <p class="step__text" style="top:5px">Prepare the liner. Cut the liner to the correct length, mix the appropriate amount of rein and impregnate the rein into the liner.</p>
      </div>
      <div class="step" style="top:319px">
        <div class="step__photo" role="img" aria-label="Technicians inverting the liner into the pipe" style="background:linear-gradient(135deg,#444,#aaa 50%,#555)"></div>
        <div class="step__num">3</div>
        <svg class="step__bracket" width="14" height="92"><path d="M13 0 L2 12 L2 80 L13 92" fill="none" stroke="#ec1f27" stroke-width="2"/></svg>
        <p class="step__text" style="top:23px">Invert the liner into the pipe, inflate and then cure.</p>
      </div>
      <div class="step" style="top:439px">
        <div class="step__photo" role="img" aria-label="Technicians curing the liner on site" style="background:linear-gradient(135deg,#3a4a2a,#888 50%,#2a2a2a)"></div>
        <div class="step__num">4</div>
        <svg class="step__bracket" width="14" height="112" style="top:-20px"><path d="M13 0 L2 12 L2 100 L13 112" fill="none" stroke="#ec1f27" stroke-width="2"/></svg>
        <p class="step__text" style="top:-16px">A seamless, flexible liner is cut to length and filled with environmentally safe epoxy rein. The liner is them inverted into the existing, host pipe and inflated using compressed air. Once the liner is fully cured with hot water, it is ready for use.</p>
      </div>

      <h2 class="tab tab--red result-tab">RESULT</h2>
      <p class="result">The result is a completely new pipe inside the old. This pipe within a pie is 100% water tight, stronger than PVC pipe, and has an increased flow rate compared to most existing pipes. Relined pipes have a life expectancy of 50 years and our installation work has a 25 year guarantee.</p>
      <div class="result-photo" role="img" aria-label="New green liner emerging from an old pipe among roots">
        <div class="step__num result-num">5</div>
      </div>

      <footer class="footer">
        <p class="footer__tag">A fast, clean, permanent<br>solution for fixing blocked drains.</p>
        <p class="footer__url">www.linewell.com.au</p>
      </footer>
    </section>
  </main>
</body>
</html>
```